QV - menu design

Hi,

We require elegant menu design for upscale restaurant. Please find attached the logo and the menu items for your reference.

for inspiration, this is a good website: -
http://www.platewhisper.example/bellfoldnotes/about.php

We are very much open for Menu Size suggestions.

unfortunately the place is going under renovation, we don't have updated images to it. the closest look and feel to our place is http://varnelo.example ..

we are also open for creative options on the shape, the styles, etc. as long as it represents the fine dine feel ...

Thanks ...

Dear All,

We wouldlike to extend our apology for not being able to provide feedbacks on everysingle design. We were extremely busy and we have multiple contests opensimultaneously which makes the process even harder.

However,we would like to thank you all for the efforts you have put into designingour menu. It is very much appreciated …

We wishyou all success in your design ventures and we are quite positive that we willbe working with many of you on many projects in the soon future. 

Thanks & Regards,

TLG Team...

 

 

 

Industry/Entity Type

Restaurant

Requirements
Must have
• Please ensure that there are 'some' images in the menu ... this is very important.
Should not have
• IMPORTANT: -

1. Please DO NOT insert any currency sign to the menu
2. Please keep the prices of the menu at the end of the menu items descriptions NOT beside the menu item names. The font of the price should be similar to the menu item description and please DO NOT bold the numbers. the prices should be subtle.

Thank you ...

```html
<!DOCTYPE html>
<html lang="en">
<head>
<meta charset="utf-8">
<title>QV – Menu</title>
<link rel="stylesheet" href="https://fonts.googleapis.com/css2?family=Montserrat:wght@300;400;500;700&display=swap">
<style>
  :root {
    --paper: #ffffff;
    --ink: #111111;
    --ink-soft: #3f3f3f;
    --rule: #cfcfcf;
    --photo-warm-a: #e9dcc8;
    --photo-warm-b: #c9a77f;
    --photo-green-a: #dfe4cf;
    --photo-green-b: #a8b27f;
    --photo-red-a: #efd6c8;
    --photo-red-b: #c47d5e;
    --line: 14.4px;
  }
  * { margin: 0; padding: 0; box-sizing: border-box; }
  html, body { width: 1200px; height: 685px; overflow: hidden; background: var(--paper); }
  .menu-spread {
    position: relative;
    width: 1200px;
    height: 685px;
    background: var(--paper);
    font-family: "Montserrat", Arial, sans-serif;
    color: var(--ink);
  }
  .menu-column {
    position: absolute;
    top: 50px;
    white-space: nowrap;
  }
  .menu-column--left { left: 56px; }
  .menu-column--right { left: 658px; }
  .column-divider {
    position: absolute;
    left: 600px;
    top: 54px;
    width: 1px;
    height: 576px;
    background: var(--rule);
  }
  .section-title {
    font-weight: 700;
    font-size: 23px;
    line-height: 28px;
    letter-spacing: 0.3px;
    margin-bottom: 29px;
  }
  .section-title--later { margin-top: 33px; }
  .dish { margin-bottom: 15.6px; }
  .dish-name {
    font-weight: 500;
    font-size: 12px;
    line-height: var(--line);
    text-transform: uppercase;
    letter-spacing: 0.3px;
  }
  .dish-desc {
    font-weight: 400;
    font-size: 11.2px;
    line-height: var(--line);
    color: var(--ink-soft);
  }
  .photo-strip {
    position: absolute;
    top: 566px;
    display: flex;
    gap: 14px;
  }
  .photo-strip--left { left: 56px; }
  .photo-strip--right { left: 658px; }
  .dish-photo {
    width: 150px;
    height: 62px;
  }
  .dish-photo--pastry { background: linear-gradient(135deg, var(--photo-warm-a), var(--photo-warm-b)); }
  .dish-photo--salad { background: linear-gradient(135deg, var(--photo-green-a), var(--photo-green-b)); }
  .dish-photo--soup { background: linear-gradient(135deg, var(--photo-red-a), var(--photo-red-b)); }
</style>
</head>
<body>
<main class="menu-spread">
  <section class="menu-column menu-column--left">
    <h2 class="section-title">THE BREAKFAST</h2>
    <div class="dish">
      <h3 class="dish-name">Butter Croisant</h3>
      <p class="dish-desc">Served plain with a selection of two jams,<br>a vanilla custard cream, a chocolate Cream and butter curls. 36</p>
    </div>
    <div class="dish">
      <h3 class="dish-name">Cheese Croissant</h3>
      <p class="dish-desc">Crumbly freshly baked with cheese filling. 29</p>
    </div>
    <div class="dish">
      <h3 class="dish-name">Daily Fresh Eggs</h3>
      <p class="dish-desc">A choice of (poached, scrambled, pan fried, omelet) all served with toasted<br>Bread, mushrooms, roasted tomatoes and chicken sausages. 59</p>
    </div>
    <div class="dish">
      <h3 class="dish-name">Healthy Time</h3>
      <p class="dish-desc">One choice of hot beverage from our cafe served with fruit salad,<br>natural yoghurt, whole wheat bread vegetable sandwiches and<br>sugar free biscuits selection. 49</p>
    </div>
    <div class="dish">
      <h3 class="dish-name">Energy Time</h3>
      <p class="dish-desc">One choice of hot beverage from our cafe served with finger chocolate muffins,<br>Poached egg with toasted bread and crispy beef bacon, crepe roll with goat<br>Cheese and honey and finger chocolate cream with salted cookies. 59</p>
    </div>
    <div class="dish">
      <h3 class="dish-name">Quiet Vale Time</h3>
      <p class="dish-desc">One choice of hot beverage from our cafe served with our selection of scones,<br>Smoked salmon and avocado sandwich, roasted sausages sandwich,<br>grilled vegetables sandwich, selection of our best biscuits. 59</p>
    </div>
    <div class="dish">
      <h3 class="dish-name">The Arabic Breakfast</h3>
      <p class="dish-desc">Choice of Zattar Manakish and Cheese Manakish, served with one choice<br>of hot beverage from our cafe and fresh orange juice. 59</p>
    </div>
  </section>

  <div class="photo-strip photo-strip--left">
    <div class="dish-photo dish-photo--pastry" role="img" aria-label="Photo of butter croissants with jams"></div>
    <div class="dish-photo dish-photo--salad" role="img" aria-label="Photo of fruit salad and yoghurt"></div>
    <div class="dish-photo dish-photo--pastry" role="img" aria-label="Photo of a hot coffee and scones"></div>
  </div>

  <div class="column-divider" aria-hidden="true"></div>

  <section class="menu-column menu-column--right">
    <h2 class="section-title">THE SANDWICH</h2>
    <div class="dish">
      <p class="dish-desc">Grilled Vegetables Sandwich with fresh Goat cheese<br>and chives served with our homemade spicy garlic mayo. 59</p>
    </div>
    <div class="dish">
      <p class="dish-desc">Butterfish burger with fresh tomato, beef bacon,<br>grilled vegetables and béarnaise sauce. 59</p>
    </div>
    <div class="dish">
      <p class="dish-desc">Tataki Tuna sandwich with red onion slices,<br>stewed endives and black olives and sultanas pate'. 79</p>
    </div>
    <div class="dish">
      <p class="dish-desc">Beef sirloin steak sandwich with grain mustard,<br>Parmesan cheese and fresh nashi pears. 79</p>
    </div>
    <div class="dish">
      <p class="dish-desc">The Traditional Club sandwich served<br>with French fries and vegetable chips. 69</p>
    </div>
    <div class="dish">
      <p class="dish-desc">Chicken sandwich with Parmesan cheese slices,<br>sundried tomatoes and mint. 79</p>
    </div>

    <h2 class="section-title section-title--later">SOUP</h2>
    <div class="dish">
      <h3 class="dish-name">Bouillabaisse</h3>
      <p class="dish-desc">Traditional French Seafood soup, with Saffron and Estragon. 119</p>
    </div>
    <div class="dish">
      <h3 class="dish-name">Barley Soup</h3>
      <p class="dish-desc">With fresh vegetables, tomato smoothie and a hint of garlic oil. 49</p>
    </div>
    <div class="dish">
      <h3 class="dish-name">Beef Chili</h3>
      <p class="dish-desc">Served with Arabic bread, fresh guacamole and spicy black beans. 49</p>
    </div>
  </section>

  <div class="photo-strip photo-strip--right">
    <div class="dish-photo dish-photo--pastry" role="img" aria-label="Photo of a club sandwich with fries"></div>
    <div class="dish-photo dish-photo--salad" role="img" aria-label="Photo of a grilled vegetables sandwich"></div>
    <div class="dish-photo dish-photo--soup" role="img" aria-label="Photo of a bowl of bouillabaisse"></div>
  </div>
</main>
</body>
</html>
```